Postcard Design

we are an environmentally safe cleaning company called Verdaplume Services, that specializes in post construction cleanup. for example, rehabbed houses and newly built commercial or residential space. we would like this mailer directed at the construction companies in order for them to call us before the property is ready to go to the buyer/client. we would like to see designs including a wood grain background and various earth toned colors (something very crisp, clean and not "flashy" marketing). It is important to convey we have flexibly with scheduling, competitive pricing, and that cleaning these properties not only enhances the contractors work but provides them with a happy customer. we are also on tobys board with a A rating and provide a 100% satisfaction guarentee

Industry/Entity Type

Construction

```html
<!DOCTYPE html>
<html lang="en">
<head>
<meta charset="utf-8">
<title>Verdaplume Services – Postcard</title>
<link rel="stylesheet" href="https://fonts.googleapis.com/css2?family=Open+Sans:wght@400;600;700&display=swap">
<style>
  :root{
    --backdrop:#1c1c1c;
    --wood:#7a4527;
    --wood-dark:#5a2f18;
    --leaf:#5fb82e;
    --leaf-light:#a6dc5c;
    --sky-top:#2d8fd6;
    --sky-bottom:#dcefff;
    --grass:#4ea82a;
    --grass-dark:#2f7a18;
    --ink:#1e1e1e;
    --ink-soft:#3a3a3a;
    --icon-green:#9ccf5a;
    --icon-green-dark:#6fae2c;
    --seal:#c8261d;
    --seal-gold:#f2c230;
    --paper:#ffffff;
    --line:#d8d8d8;
    --stamp:#ececec;
  }
  *{box-sizing:border-box;margin:0;padding:0}
  html,body{width:976px;height:1200px;overflow:hidden}
  body{background:var(--backdrop);font-family:"Open Sans",Arial,sans-serif;color:var(--ink);position:relative}

  .postcard{position:absolute;left:108px;width:760px;height:520px;overflow:hidden;background:var(--paper)}
  .postcard--front{top:60px}
  .postcard--back{top:620px}

  .sky{position:absolute;background:linear-gradient(180deg,var(--sky-top),var(--sky-bottom) 85%)}
  .wood-band{position:absolute;background:linear-gradient(90deg,var(--wood-dark),var(--wood) 30%,#8b5230 60%,var(--wood-dark))}
  .grass{position:absolute;background:linear-gradient(180deg,var(--leaf-light),var(--grass) 40%,var(--grass-dark))}
  .leaves{position:absolute;background:linear-gradient(90deg,var(--leaf),var(--leaf-light) 50%,var(--leaf))}

  .brand{position:absolute;background:var(--paper);border-radius:10px;display:flex;align-items:center;gap:8px;padding:0 14px;box-shadow:0 2px 4px rgba(0,0,0,.25)}
  .brand__dot{width:16px;height:16px;border-radius:50%;background:var(--leaf)}
  .brand__name{font-weight:700;color:var(--ink-soft);font-size:26px;letter-spacing:-.5px}

  .seal{position:absolute;right:50px;top:12px;width:92px;height:92px;border-radius:50%;background:var(--seal);border:6px solid var(--seal-gold)}

  .about{position:absolute;left:40px;top:150px;width:680px}
  .about h2{font-size:17px;font-weight:700;line-height:1.1}
  .about p{font-size:13.5px;line-height:1.25}
  .services{position:absolute;left:40px;top:205px}
  .services h2{font-size:17px;font-weight:700;line-height:1.1}
  .services li{list-style:none;font-size:14.5px;line-height:1.2;padding-left:8px}

  .house{position:absolute;left:390px;top:200px;width:350px;height:215px;background:linear-gradient(180deg,#cfd9e6 0%,#e3c9a2 35%,#d6b486 75%,#5aa030 100%);border-radius:2px}

  .benefits{position:absolute;left:36px;top:300px;display:flex;gap:18px}
  .benefit{width:96px;display:flex;flex-direction:column;align-items:center}
  .benefit__icon{width:72px;height:72px;border-radius:50%;background:var(--icon-green);display:flex;align-items:center;justify-content:center;color:var(--paper);font-weight:700;font-size:30px}
  .benefit__label{margin-top:-6px;background:var(--icon-green-dark);color:var(--paper);border:2px solid var(--paper);border-radius:8px;font-size:11px;font-weight:600;line-height:1.1;text-align:center;padding:3px 6px;width:92px}

  .back-photo{position:absolute;left:0;top:0;width:330px;height:520px;overflow:hidden}
  .back-tagline{position:absolute;left:40px;top:250px;width:250px;text-align:center;font-size:19px;font-weight:700;line-height:1.15;color:var(--ink)}
  .stamp-box{position:absolute;right:40px;top:30px;width:110px;height:95px;background:var(--stamp)}
  .address-lines{position:absolute;left:390px;top:250px;width:330px}
  .address-lines span{display:block;height:1px;background:var(--line);margin-bottom:40px}
</style>
</head>
<body>

<section class="postcard postcard--front" aria-label="Postcard front">
  <div class="sky" style="left:0;top:90px;width:760px;height:340px"></div>
  <div class="wood-band" role="img" aria-label="Wood grain band" style="left:0;top:0;width:760px;height:110px"></div>
  <div class="leaves" role="img" aria-label="Green leaves with water droplets" style="left:0;top:0;width:760px;height:28px"></div>
  <div class="house" role="img" aria-label="Photo of a newly built two-storey house"></div>
  <div class="grass" role="img" aria-label="Green lawn" style="left:0;top:400px;width:760px;height:60px"></div>
  <div class="wood-band" role="img" aria-label="Wood grain band" style="left:0;top:455px;width:760px;height:65px"></div>
  <div class="leaves" role="img" aria-label="Green leaves with water droplets" style="left:0;top:440px;width:760px;height:30px"></div>

  <div class="brand" style="left:30px;top:38px;height:62px"><span class="brand__dot"></span><span class="brand__name">Verdaplume</span></div>
  <div class="seal" role="img" aria-label="Guarantee seal"></div>

  <div class="about">
    <h2>About US</h2>
    <p>we are an environmentally safe cleaning company that specializes in post construction cleanup.</p>
  </div>
  <div class="services">
    <h2>Our Services</h2>
    <ul>
      <li>-- rehabbed houses</li>
      <li>-- newly built commercial</li>
      <li>-- residential space</li>
    </ul>
  </div>

  <div class="benefits">
    <div class="benefit">
      <div class="benefit__icon">
        <svg width="40" height="36" viewBox="0 0 40 36" aria-hidden="true"><rect x="2" y="6" width="36" height="28" rx="3" fill="none" stroke="#fff" stroke-width="3"/><line x1="2" y1="14" x2="38" y2="14" stroke="#fff" stroke-width="3"/><line x1="11" y1="1" x2="11" y2="9" stroke="#fff" stroke-width="3"/><line x1="29" y1="1" x2="29" y2="9" stroke="#fff" stroke-width="3"/></svg>
      </div>
      <div class="benefit__label">flexibly with scheduling</div>
    </div>
    <div class="benefit">
      <div class="benefit__icon">$</div>
      <div class="benefit__label">competitive pricing</div>
    </div>
    <div class="benefit">
      <div class="benefit__icon"></div>
      <div class="benefit__label">happy customer</div>
    </div>
  </div>
</section>

<section class="postcard postcard--back" aria-label="Postcard back">
  <div class="back-photo">
    <div class="sky" style="left:0;top:90px;width:330px;height:320px"></div>
    <div class="wood-band" role="img" aria-label="Wood grain band" style="left:0;top:0;width:330px;height:110px"></div>
    <div class="leaves" role="img" aria-label="Green leaves with water droplets" style="left:0;top:0;width:330px;height:26px"></div>
    <div class="grass" role="img" aria-label="Green lawn" style="left:0;top:400px;width:330px;height:50px"></div>
    <div class="wood-band" role="img" aria-label="Wood grain band" style="left:0;top:445px;width:330px;height:75px"></div>
    <div class="brand" style="left:80px;top:40px;height:56px"><span class="brand__dot"></span><span class="brand__name">Verdaplume</span></div>
    <p class="back-tagline">environmentally safe cleaning company that specializes in post construction cleanup</p>
  </div>
  <div class="stamp-box"></div>
  <div class="address-lines"><span></span><span></span><span></span><span></span></div>
</section>

</body>
</html>
```